Highly rated moving company needs postcard design

We need a highly converting postcard to send when people put their homes for sale online. This should highlight the fact that we're Austin's highest rated moving company, and should convey quality and value. We do local, statewide and long distance moves. We also do office and commerical moves and storage. final design must be sized to work with our mailing system. Please see attached file for more information.

```html
<!DOCTYPE html>
<html lang="en">
<head>
<meta charset="utf-8">
<title>Ridgeline Movers Postcard</title>
<link href="https://fonts.googleapis.com/css2?family=Montserrat:wght@400;500;600;700;800;900&display=swap" rel="stylesheet">
<style>
:root{
  --navy:#262767;
  --red:#e3212b;
  --paper:#f4f4f4;
  --ink:#2b2b3a;
  --grey:#c9c9c9;
  --soft:#e4e4e8;
}
*{box-sizing:border-box;margin:0;padding:0}
html,body{width:1200px;height:900px;overflow:hidden}
body{background:var(--grey);font-family:"Montserrat",Arial,sans-serif;color:var(--ink);position:relative}
.card{position:absolute;left:300px;width:600px;height:400px;background:var(--paper);box-shadow:0 4px 14px rgba(0,0,0,.18);overflow:hidden}
.card--front{top:40px;display:grid;grid-template-columns:272px 1fr}
.card--back{top:460px;display:grid;grid-template-columns:418px 1fr}

.brand{display:flex;align-items:center;gap:6px;font-weight:800;color:var(--navy);font-size:17px;line-height:1}
.brand__dot{width:14px;height:14px;border-radius:50%;background:var(--red)}

/* front left */
.front-info{display:flex;flex-direction:column;padding:14px 0 0 0}
.front-info .brand{padding-left:14px}
.headline-band{margin:10px 0 0;background:var(--red);color:#fff;font-weight:900;font-size:21px;line-height:1.05;padding:9px 14px;text-transform:uppercase;letter-spacing:.3px}
.intro{padding:9px 14px 0}
.intro h2{color:var(--navy);font-size:14px;font-weight:800}
.intro p,.expect p{font-size:7.6px;line-height:1.4;margin-top:2px}
.diff{padding:8px 14px 0}
.diff h3,.expect h3{color:var(--navy);font-size:9.5px;font-weight:800;line-height:1.2}
.features{display:flex;justify-content:space-between;margin-top:6px}
.feature{display:flex;align-items:center;gap:4px;font-size:7px;font-weight:700;line-height:1.15;width:33%}
.feature svg{flex:none}
.expect{padding:9px 14px 0}
.contact-bar{margin-top:auto;background:var(--navy);color:#fff;display:flex;gap:12px;align-items:center;padding:6px 14px;font-size:8.5px;font-weight:600}
.contact-bar .phone{display:flex;align-items:center;gap:3px}
.contact-bar .phone--main{font-size:10.5px;font-weight:800}

/* front right */
.front-visual{display:flex;flex-direction:column}
.photo{background:linear-gradient(135deg,#eae7e4 0%,#cfc8c2 45%,#3a3f5c 75%,#6a3a44 100%)}
.photo--family{height:262px}
.quote-band{background:var(--red);color:#fff;font-weight:900;font-size:15px;text-transform:uppercase;padding:7px 12px;letter-spacing:.4px}
.badges{display:flex;align-items:center;justify-content:space-between;padding:8px 12px;flex:1}
.badge{background:var(--soft);border-radius:4px;height:26px}
.badge--round{width:26px;border-radius:50%}
.address-bar{background:var(--navy);color:#fff;font-size:8px;font-weight:500;padding:6px 12px;display:flex;gap:4px;align-items:center}

/* back left */
.services{padding:12px 0 0 14px;display:flex;flex-direction:column}
.services h2{color:var(--red);font-size:15px;font-weight:900;text-transform:uppercase}
.services .lede{font-size:7.6px;line-height:1.35;margin-top:2px;padding-right:4px}
.tiles{display:grid;grid-template-columns:repeat(4,1fr);gap:4px;margin-top:7px;padding-right:4px}
.tile__label{background:var(--navy);color:#fff;font-size:7.4px;font-weight:700;padding:3px 4px;text-align:center}
.tile .photo{height:68px;background:linear-gradient(135deg,#f1ece6,#c9a57c)}
.tile:nth-child(2) .photo{background:linear-gradient(135deg,#dfe6ee,#b98f62)}
.tile:nth-child(3) .photo{background:linear-gradient(135deg,#e8ded6,#c49a70)}
.tile:nth-child(4) .photo{background:linear-gradient(135deg,#efe7df,#b78958)}
.choose{background:var(--red);color:#fff;margin:7px 0 0 -14px;padding:7px 14px}
.choose h3{font-size:13px;font-weight:800}
.choose p{font-size:7.2px;line-height:1.4;margin-top:2px}
.areas{padding:7px 0 0}
.areas h4{color:var(--navy);font-size:10px;font-weight:800;text-transform:uppercase}
.area-cols{display:grid;grid-template-columns:repeat(3,1fr);margin-top:3px}
.area-cols ul{list-style:none}
.area-cols li{font-size:7.6px;font-weight:600;display:flex;align-items:center;gap:3px;line-height:1.45}
.zones{display:flex;gap:10px;margin-top:6px}
.zone{display:flex;gap:4px;align-items:flex-start;font-size:6.4px;line-height:1.3;width:33%}
.zone strong{color:var(--red);font-size:7.2px;display:block}
.back-bar{margin:auto 0 0 -14px;background:var(--navy);color:#fff;display:flex;gap:12px;align-items:center;padding:5px 14px;font-size:8px;font-weight:600}

/* back right */
.mailing{position:relative;padding:14px 14px 0 10px;display:flex;flex-direction:column;align-items:flex-start}
.stamp{align-self:flex-end;width:46px;height:54px;border:1px solid #9a9aa6}
.mailing .brand{margin-top:36px;font-size:15px}
.photo--map{width:150px;height:96px;margin-top:18px;background:linear-gradient(135deg,#f3f0e2,#dcdcc8);border:1px solid #bdbdbd}
.mailing .zone{width:auto;margin-top:8px}
</style>
</head>
<body>

<section class="card card--front" aria-label="Postcard front">
  <div class="front-info">
    <div class="brand"><span class="brand__dot"></span>Ridgeline Movers</div>
    <h1 class="headline-band">Let our family<br>move yours</h1>
    <div class="intro">
      <h2>Austin Movers</h2>
      <p>Austinites rave about our moving help. We're proud to be the most dependable moving company in Austin.</p>
    </div>
    <div class="diff">
      <h3>What makes us different from other moving companies in Austin, TX?</h3>
      <div class="features">
        <div class="feature">
          <svg width="16" height="16" viewBox="0 0 16 16"><circle cx="8" cy="8" r="7" fill="var(--red)"/><path d="M4.5 8.2l2.3 2.3 4.7-4.8" stroke="#fff" stroke-width="1.6" fill="none"/></svg>
          Worry Free Damage Guarantee
        </div>
        <div class="feature">
          <svg width="16" height="16" viewBox="0 0 16 16"><circle cx="8" cy="8" r="7" fill="var(--red)"/><path d="M8 4v4l3 2" stroke="#fff" stroke-width="1.6" fill="none"/></svg>
          On Time Guarantee
        </div>
        <div class="feature">
          <svg width="16" height="16" viewBox="0 0 16 16"><circle cx="8" cy="8" r="7" fill="var(--red)"/><path d="M10 5.5H7a1.3 1.3 0 000 2.6h2a1.3 1.3 0 010 2.6H6M8 4v8" stroke="#fff" stroke-width="1.3" fill="none"/></svg>
          No Hidden Fees
        </div>
      </div>
    </div>
    <div class="expect">
      <h3>What You Can Expect During Your Move</h3>
      <p>Let's talk about the cost of your upcoming move. As your trusted relocation company in Austin, we're always transparent and honest about pricing. We don't tolerate hidden fees and are upfront from the start. There are no surprises when you choose us.</p>
    </div>
    <div class="contact-bar">
      <span class="phone phone--main"><svg width="9" height="9" viewBox="0 0 10 10"><circle cx="5" cy="5" r="5" fill="var(--red)"/></svg>512-555-0141</span>
      <span class="phone"><svg width="8" height="8" viewBox="0 0 10 10"><circle cx="5" cy="5" r="5" fill="var(--red)"/></svg>512-555-0187</span>
    </div>
  </div>

  <div class="front-visual">
    <div class="photo photo--family" role="img" aria-label="Smiling family of three embracing in a bright new home"></div>
    <div class="quote-band">Get a free moving quote</div>
    <div class="badges">
      <span class="badge" style="width:62px"></span>
      <span class="badge" style="width:54px"></span>
      <span class="badge badge--round"></span>
      <span class="badge" style="width:50px"></span>
      <span class="badge" style="width:40px"></span>
    </div>
    <div class="address-bar">
      <svg width="8" height="10" viewBox="0 0 8 10"><path d="M4 0a3.5 3.5 0 00-3.5 3.5C.5 6 4 10 4 10s3.5-4 3.5-6.5A3.5 3.5 0 004 0z" fill="var(--red)"/></svg>
      4200 Cedar Bend Dr Suite 210, Austin, TX 78759
    </div>
    <div class="address-bar" style="border-top:1px solid rgba(255,255,255,.15)">www.ridgelinemoversatx.com</div>
  </div>
</section>

<section class="card card--back" aria-label="Postcard back">
  <div class="services">
    <h2>Moving services we offer</h2>
    <p class="lede">Whether you're moving across the street or across the state, we'll make sure your move is stress-free and efficient. We'll take care of everything from packing to furniture assembly, so you can relax and focus on your new home.</p>
    <div class="tiles">
      <div class="tile"><div class="tile__label">Residential Moving</div><div class="photo" role="img" aria-label="Living room filled with moving boxes"></div></div>
      <div class="tile"><div class="tile__label">Commercial Moving</div><div class="photo" role="img" aria-label="Mover carrying boxes in an office"></div></div>
      <div class="tile"><div class="tile__label">Packing Services</div><div class="photo" role="img" aria-label="Hands taping a cardboard box"></div></div>
      <div class="tile"><div class="tile__label">Piano Moving</div><div class="photo" role="img" aria-label="Stacked boxes in a new home"></div></div>
    </div>
    <div class="choose">
      <h3>Choose Ridgeline Movers</h3>
      <p>Ridgeline Movers is the No. 1 choice for residential and commercial moving labor in the Austin area. We're a moving company founded on the core values of honesty, dependability, adaptability, &amp; respect. Hire us, and you know you're getting the strongest &amp; most reliable moving team in the city. We dare say that we do more than provide stress-free moves — we make moving fun!</p>
    </div>
    <div class="areas">
      <h4>Areas we serve</h4>
      <div class="area-cols">
        <ul>
          <li><svg width="7" height="7" viewBox="0 0 8 8"><rect x=".5" y=".5" width="7" height="7" fill="none" stroke="var(--navy)"/><path d="M1.8 4l1.5 1.5L6.3 2.3" stroke="var(--navy)" fill="none"/></svg>Austin</li>
          <li><svg width="7" height="7" viewBox="0 0 8 8"><rect x=".5" y=".5" width="7" height="7" fill="none" stroke="var(--navy)"/><path d="M1.8 4l1.5 1.5L6.3 2.3" stroke="var(--navy)" fill="none"/></svg>Bee Cave</li>
          <li><svg width="7" height="7" viewBox="0 0 8 8"><rect x=".5" y=".5" width="7" height="7" fill="none" stroke="var(--navy)"/><path d="M1.8 4l1.5 1.5L6.3 2.3" stroke="var(--navy)" fill="none"/></svg>Buda</li>
          <li><svg width="7" height="7" viewBox="0 0 8 8"><rect x=".5" y=".5" width="7" height="7" fill="none" stroke="var(--navy)"/><path d="M1.8 4l1.5 1.5L6.3 2.3" stroke="var(--navy)" fill="none"/></svg>Hutto</li>
          <li><svg width="7" height="7" viewBox="0 0 8 8"><rect x=".5" y=".5" width="7" height="7" fill="none" stroke="var(--navy)"/><path d="M1.8 4l1.5 1.5L6.3 2.3" stroke="var(--navy)" fill="none"/></svg>Lakeway</li>
          <li><svg width="7" height="7" viewBox="0 0 8 8"><rect x=".5" y=".5" width="7" height="7" fill="none" stroke="var(--navy)"/><path d="M1.8 4l1.5 1.5L6.3 2.3" stroke="var(--navy)" fill="none"/></svg>Leander</li>
        </ul>
        <ul>
          <li><svg width="7" height="7" viewBox="0 0 8 8"><rect x=".5" y=".5" width="7" height="7" fill="none" stroke="var(--navy)"/><path d="M1.8 4l1.5 1.5L6.3 2.3" stroke="var(--navy)" fill="none"/></svg>Brushy Creek</li>
          <li><svg width="7" height="7" viewBox="0 0 8 8"><rect x=".5" y=".5" width="7" height="7" fill="none" stroke="var(--navy)"/><path d="M1.8 4l1.5 1.5L6.3 2.3" stroke="var(--navy)" fill="none"/></svg>Georgetown</li>
          <li><svg width="7" height="7" viewBox="0 0 8 8"><rect x=".5" y=".5" width="7" height="7" fill="none" stroke="var(--navy)"/><path d="M1.8 4l1.5 1.5L6.3 2.3" stroke="var(--navy)" fill="none"/></svg>North Austin</li>
          <li><svg width="7" height="7" viewBox="0 0 8 8"><rect x=".5" y=".5" width="7" height="7" fill="none" stroke="var(--navy)"/><path d="M1.8 4l1.5 1.5L6.3 2.3" stroke="var(--navy)" fill="none"/></svg>Round Rock</li>
          <li><svg width="7" height="7" viewBox="0 0 8 8"><rect x=".5" y=".5" width="7" height="7" fill="none" stroke="var(--navy)"/><path d="M1.8 4l1.5 1.5L6.3 2.3" stroke="var(--navy)" fill="none"/></svg>South Austin</li>
          <li><svg width="7" height="7" viewBox="0 0 8 8"><rect x=".5" y=".5" width="7" height="7" fill="none" stroke="var(--navy)"/><path d="M1.8 4l1.5 1.5L6.3 2.3" stroke="var(--navy)" fill="none"/></svg>West Lake Hills</li>
        </ul>
        <ul>
          <li><svg width="7" height="7" viewBox="0 0 8 8"><rect x=".5" y=".5" width="7" height="7" fill="none" stroke="var(--navy)"/><path d="M1.8 4l1.5 1.5L6.3 2.3" stroke="var(--navy)" fill="none"/></svg>Cedar Park</li>
          <li><svg width="7" height="7" viewBox="0 0 8 8"><rect x=".5" y=".5" width="7" height="7" fill="none" stroke="var(--navy)"/><path d="M1.8 4l1.5 1.5L6.3 2.3" stroke="var(--navy)" fill="none"/></svg>Liberty Hill</li>
          <li><svg width="7" height="7" viewBox="0 0 8 8"><rect x=".5" y=".5" width="7" height="7" fill="none" stroke="var(--navy)"/><path d="M1.8 4l1.5 1.5L6.3 2.3" stroke="var(--navy)" fill="none"/></svg>Manchaca</li>
          <li><svg width="7" height="7" viewBox="0 0 8 8"><rect x=".5" y=".5" width="7" height="7" fill="none" stroke="var(--navy)"/><path d="M1.8 4l1.5 1.5L6.3 2.3" stroke="var(--navy)" fill="none"/></svg>Pflugerville</li>
        </ul>
      </div>
      <div class="zones">
        <div class="zone"><svg width="12" height="14" viewBox="0 0 8 10"><path d="M4 0a3.5 3.5 0 00-3.5 3.5C.5 6 4 10 4 10s3.5-4 3.5-6.5A3.5 3.5 0 004 0z" fill="none" stroke="var(--red)"/></svg><span><strong>North Austin</strong>We serve the entire area of north Austin.</span></div>
        <div class="zone"><svg width="12" height="14" viewBox="0 0 8 10"><path d="M4 0a3.5 3.5 0 00-3.5 3.5C.5 6 4 10 4 10s3.5-4 3.5-6.5A3.5 3.5 0 004 0z" fill="none" stroke="var(--red)"/></svg><span><strong>South Austin</strong>We serve the entire area of south Austin.</span></div>
      </div>
    </div>
    <div class="back-bar">
      <span>512-555-0141</span><span>512-555-0187</span><span>www.ridgelinemoversatx.com</span>
    </div>
  </div>

  <div class="mailing">
    <div class="stamp" aria-label="Postage area"></div>
    <div class="brand"><span class="brand__dot"></span>Ridgeline Movers</div>
    <div class="photo photo--map" role="img" aria-label="Map of the Austin area with the service radius circled"></div>
    <div class="zone"><svg width="12" height="14" viewBox="0 0 8 10"><path d="M4 0a3.5 3.5 0 00-3.5 3.5C.5 6 4 10 4 10s3.5-4 3.5-6.5A3.5 3.5 0 004 0z" fill="none" stroke="var(--red)"/></svg><span><strong>Travis/Williamson County</strong>We serve the entire area of Travis/Williamson County.</span></div>
  </div>
</section>

</body>
</html>
```